Layout for site fence advertising - length approx. 250 cm x 125 cm

The advertising will later be printed on a PVC film and used for events or on sports fields.

Main services :
Your regional contact at
Real estate and business financing
independent insurance advice

```html
<!DOCTYPE html>
<html lang="en">
<head>
<meta charset="UTF-8">
<title>NR Finanzberatung GmbH – Fence Banner</title>
<link rel="stylesheet" href="https://fonts.googleapis.com/css2?family=Questrial&family=Saira+Condensed:wght@700;800&display=swap">
<style>
  :root {
    --brand-blue: #1a55bd;
    --text-gray: #555555;
    --band-gray: #646464;
    --ring-gray: #cccccc;
    --paper: #ffffff;
    --stage-dark: #2e2e2e;
    --stage-light: #8a8a8a;
    --suit-dark: #2a2838;
    --skin-tone: #d9a48c;
  }
  html, body {
    margin: 0;
    padding: 0;
    width: 1000px;
    height: 1200px;
    overflow: hidden;
  }
  body {
    background: radial-gradient(ellipse at center, var(--stage-light) 0%, var(--stage-dark) 85%);
    position: relative;
  }
  .banner {
    position: absolute;
    left: 30px;
    top: 365px;
    width: 940px;
    height: 470px;
    background: var(--paper);
    box-shadow: 0 12px 40px rgba(0,0,0,0.55);
  }
  .banner svg { display: block; }
  .brand-name {
    font-family: "Questrial", sans-serif;
    font-size: 21px;
    fill: var(--brand-blue);
  }
  .brand-tagline {
    font-family: "Questrial", sans-serif;
    font-size: 15.5px;
    fill: var(--text-gray);
  }
  .services-title {
    font-family: "Saira Condensed", sans-serif;
    font-weight: 800;
    font-size: 40px;
    letter-spacing: 2px;
    fill: var(--brand-blue);
  }
  .service-item {
    font-family: "Saira Condensed", sans-serif;
    font-weight: 700;
    font-size: 25px;
    fill: var(--text-gray);
  }
  .phone-number {
    font-family: "Saira Condensed", sans-serif;
    font-weight: 800;
    font-size: 58px;
    letter-spacing: 6px;
    fill: var(--paper);
  }
  .web-address {
    font-family: "Saira Condensed", sans-serif;
    font-weight: 800;
    font-size: 32px;
    letter-spacing: 5px;
    fill: var(--paper);
  }
</style>
</head>
<body>
  <div class="banner">
    <svg width="940" height="470" viewBox="0 0 940 470">
      <defs>
        <linearGradient id="portrait-tone" x1="0" y1="0" x2="0" y2="1">
          <stop offset="0" stop-color="var(--skin-tone)"/>
          <stop offset="0.5" stop-color="#b98c7a"/>
          <stop offset="0.62" stop-color="var(--suit-dark)"/>
          <stop offset="1" stop-color="var(--suit-dark)"/>
        </linearGradient>
      </defs>

      <!-- decorative ring behind portrait -->
      <circle class="decor-ring" cx="721" cy="224" r="219" fill="none" stroke="var(--ring-gray)" stroke-width="10"/>

      <!-- brand block -->
      <circle class="brand-circle" cx="112" cy="98" r="56" fill="none" stroke="var(--brand-blue)" stroke-width="4"/>
      <line class="brand-divider" x1="181" y1="39" x2="181" y2="158" stroke="var(--band-gray)" stroke-width="3"/>
      <text class="brand-name" x="191" y="92">NR Finanzberatung GmbH</text>
      <text class="brand-tagline" x="191" y="116">Finanzieren, Versichern, Vorsorgen</text>

      <!-- services -->
      <text class="services-title" x="54" y="224">MAIN SERVICES :</text>
      <g class="service-list">
        <circle cx="60" cy="253" r="4.5" fill="var(--brand-blue)"/>
        <text class="service-item" x="70" y="262">YOUR REGIONAL CONTACT AT</text>
        <circle cx="60" cy="287" r="4.5" fill="var(--brand-blue)"/>
        <text class="service-item" x="70" y="296">REAL ESTATE AND BUSINESS FINANCING</text>
        <circle cx="60" cy="321" r="4.5" fill="var(--brand-blue)"/>
        <text class="service-item" x="70" y="330">INDEPENDENT INSURANCE ADVICE</text>
      </g>

      <!-- contact bands -->
      <rect class="phone-band" x="0" y="352" width="720" height="60" fill="var(--brand-blue)"/>
      <rect class="web-band" x="0" y="415" width="720" height="55" fill="var(--band-gray)"/>
      <text class="phone-number" x="56" y="405">123-456-2100</text>
      <text class="web-address" x="54" y="458">WWW.YOURWEBSITE.COM</text>

      <!-- portrait area -->
      <path class="portrait" role="img" aria-label="Portrait photo of the advisor in a dark suit and white shirt"
            d="M695 470 L720 395 Q740 340 800 320 L790 300 Q745 270 745 160 Q745 20 830 18 Q915 20 915 160 Q915 260 880 300 L890 320 Q935 335 940 345 L940 470 Z"
            fill="url(#portrait-tone)"/>
    </svg>
  </div>
</body>
</html>
```